Personal Business Card

Looking for a clean and modern personal business card. Basically I need something catchy to give to potential clients and people I meet. I do a lot of freelancing (from DJ'ing to wedding videography, but its mostly on the event side of things) so it's more-so about selling myself rather than identifying with a company. I'm starting to meet more people that I want to work with after meeting them so I'm revamping my business cards.

I'm looking for a clean and modern design- I know that's really vague but I'm fine with anything ranging from a symbol to just a fancy version of my name.

Details I need on the front:
Dennis Kowal
dennis@denniskowal-mail.net
(555) 807-2291

On the back I'd like to have something simple like "Nice to have met you today" or "Great meeting you".

UPDATE 9/27 Noon: My apologies for not putting it up before- I'm definitely looking for full color. Doesn't have to be a rainbow but I am looking for the least amount of blank white as possible.

UPDATE 10/1: Really impressed with what I've been getting so far and I'm working on giving everyone feedback- if your design is still up then you're still in the run. Looking for something more unique and modern so please do not post something that looks like a template from Cardloom!

Target Market(s)

Mainly to give to people aged 18-35. Most of my encounters will be casual so the card should have a "young" feeling to it. I rarely do anything in the corporate world so it doesn't have to be boring. It should give the impression that I'm the one they should go to if they need what I do (again it changes every weekend so I'll probably say the "what I do" part.

Industry/Entity Type

Wedding

Requirements
Must have
• Basically the contact information listed above
Nice to have
• I really like the colors Blue, Silver, and Purple. They don't have to necessarily all be there though. I do like the look of polished metal if that makes sense.
Should not have
• A template that resembles card-loom. I'm in a point in my life where I'm working a lot of different markets/areas so the card does not need to have an address or address placeholder.

```html
<!DOCTYPE html>
<html lang="en">
<head>
<meta charset="utf-8">
<title>Dennis Kowal — Business Card</title>
<link rel="stylesheet" href="https://fonts.googleapis.com/css2?family=Source+Sans+3:wght@400;500&display=swap">
<style>
  :root {
    --card-blue: #02029a;
    --swoosh-blue: #2b2bb8;
    --name-cyan: #35f2ff;
    --ink-white: #ffffff;
  }
  html, body {
    margin: 0;
    padding: 0;
    width: 667px;
    height: 1200px;
    overflow: hidden;
    background: var(--card-blue);
  }
  .card {
    position: relative;
    width: 667px;
    height: 1200px;
    background: var(--card-blue);
    overflow: hidden;
    font-family: "Source Sans 3", "Myriad Pro", sans-serif;
    color: var(--ink-white);
  }
  .swoosh {
    position: absolute;
    inset: 0;
    width: 667px;
    height: 1200px;
  }
  .name {
    position: absolute;
    left: 0;
    right: 0;
    top: 150px;
    margin: 0;
    text-align: center;
    font-family: "Source Sans 3", "Myriad Pro", sans-serif;
    font-weight: 500;
    font-size: 128px;
    line-height: 150px;
    color: var(--name-cyan);
  }
  .name-line { display: block; }
  .services {
    position: absolute;
    left: 0;
    right: 0;
    top: 588px;
    margin: 0;
    text-align: center;
    font-size: 46px;
    font-weight: 400;
    line-height: 68px;
  }
  .contact {
    position: absolute;
    left: 0;
    right: 0;
    top: 822px;
    margin: 0;
    text-align: center;
    font-size: 40px;
    line-height: 56px;
    font-style: normal;
  }
  .contact-item { display: block; }
  .contact-item + .contact-item { margin-top: 50px; }
  .contact-label, .contact-value { display: block; }
</style>
</head>
<body>
  <main class="card">
    <svg class="swoosh" viewBox="0 0 667 1200" aria-hidden="true">
      <path d="M424 0 C470 120 500 260 520 420 C540 600 520 820 500 1000 C492 1080 486 1150 482 1200 L540 1200 C545 1120 555 1040 566 960 C590 780 592 600 570 430 C552 280 500 130 440 0 Z" fill="var(--swoosh-blue)"/>
      <path d="M430 0 C470 90 505 170 530 260" fill="none" stroke="var(--swoosh-blue)" stroke-width="3"/>
    </svg>

    <h1 class="name">
      <span class="name-line">DENNIS</span>
      <span class="name-line">Kowal</span>
    </h1>

    <p class="services">Freelance DJ<br>Videographer</p>

    <address class="contact">
      <span class="contact-item">
        <span class="contact-label">Tel.</span>
        <span class="contact-value">(555) 807-2291</span>
      </span>
      <span class="contact-item">
        <span class="contact-label">Email</span>
        <span class="contact-value">dennis@denniskowal-mail.net</span>
      </span>
    </address>
  </main>
</body>
</html>
```